Elegant wine label

Looking for a new Napa Valley wine label called "Velmira". Our wines will retail for $150 + per bottle. Velmira is derived from the greek word Ergo (therefore) tied in with Air for aeration for wine.

We handcraft our small production wine. 200 cases.
Looking for a very sophisticated, minimalist elegant look. Wine labels we like for inspiration and reference include: www.trelk.wine, www.plavicwine.com, www.morvinestates.com, www.dunleafywine.com, www.kretavine.com/Wine, https://shop.gavrelwine.com/wine

Colors will include white, black and blue foil (Approx. color: C 94.9, M 83.53, Y 0, K 0). We want a custom-created, minimal greek/roman looking font for lettering.

```html
<!DOCTYPE html>
<html lang="en">
<head>
<meta charset="utf-8">
<title>Velmira – Napa Valley Wine Label</title>
<link rel="stylesheet" href="https://fonts.googleapis.com/css2?family=Bodoni+Moda:opsz,wght@6..96,400;6..96,500&display=swap">
<style>
  :root {
    --page-bg: #f3f3f4;
    --label-black: #070508;
    --label-white: #ffffff;
    --blue-deep: #0c1d6b;
    --blue-mid: #2a47b8;
    --blue-light: #7f9be6;
    --blue-pale: #c3d0f4;
  }
  * { margin: 0; padding: 0; box-sizing: border-box; }
  html, body {
    width: 675px;
    height: 1200px;
    overflow: hidden;
    background: var(--page-bg);
  }
  .canvas {
    position: relative;
    width: 675px;
    height: 1200px;
    display: flex;
    align-items: center;
    justify-content: center;
  }
  .wine-label {
    position: relative;
    width: 306px;
    height: 1080px;
    background: var(--label-black);
    box-shadow: 0 6px 24px rgba(0, 0, 0, 0.18);
  }
  .label-artwork {
    position: absolute;
    top: 0;
    left: 0;
    width: 100%;
    height: 400px;
    background:
      radial-gradient(ellipse at 55% 35%, var(--blue-pale) 0%, rgba(195, 208, 244, 0) 38%),
      radial-gradient(ellipse at 30% 70%, var(--blue-light) 0%, rgba(127, 155, 230, 0) 45%),
      linear-gradient(155deg, var(--blue-mid) 0%, var(--blue-deep) 55%, var(--blue-mid) 80%, var(--blue-deep) 100%);
  }
  .brand-name {
    position: absolute;
    top: 600px;
    left: 0;
    width: 100%;
    text-align: center;
    font-family: "Bodoni Moda", "Didot", serif;
    font-weight: 400;
    font-size: 60px;
    line-height: 1;
    letter-spacing: -1px;
    color: var(--label-white);
  }
  .appellation {
    position: absolute;
    top: 878px;
    left: 0;
    width: 100%;
    text-align: center;
    font-family: "Bodoni Moda", "Didot", serif;
    font-weight: 500;
    font-size: 11px;
    line-height: 1.3;
    letter-spacing: 2px;
    color: var(--label-white);
  }
  .vintage {
    position: absolute;
    top: 962px;
    left: 0;
    width: 100%;
    text-align: center;
    font-family: "Bodoni Moda", "Didot", serif;
    font-weight: 400;
    font-size: 17px;
    letter-spacing: 6px;
    color: var(--label-white);
  }
</style>
</head>
<body>
  <main class="canvas">
    <article class="wine-label">
      <div class="label-artwork" role="img" aria-label="Abstract palette-knife painting in layered blue brushstrokes, resembling a feather or wing"></div>
      <h1 class="brand-name">Velmira</h1>
      <p class="appellation">NAPA VALLEY<br>CALIFORNIA</p>
      <p class="vintage">2025</p>
    </article>
  </main>
</body>
</html>
```